Design Our Full Stationary Set

Hi, I require a selection of complimentary stationary as outlined below. The winning design to be provided .eps and .svg of each. We are in the advertising sphere, the winning design should be artistic, colourful, attractive and grab your attention. Files attached.

All should be 300 DPI

Business Card - 2 Sides
Full Bleed Size 88x58mm (1040x685 pixels)
Safe Margin Size for Text 85x55mm (1004x650 pixels)

Folder
Full Bleed Size 53x42.4cm (6260x5004 pixels)
Safe Margin Size for Text 52.7x42.1cm (6225x4969 pixels)

Address Label
Full Bleed Size 90x52mm (1062x615 pixels)
Safe Margin Size for Text 87x49mm (1028x579 pixels)

Envelope Seal (CIRCLE)
Full Bleed Size 43mm diameter (510 pixels)
Safe Margin Size for Text 38mm diameter (450 pixels)

Letterhead
Full Bleed Size 213x300mm (2517x3544 pixels)
Safe Margin Size for Text 210x297mm (2480x3580 pixels)

INFORMATION:

Company Name: Vexley Quill Ltd.
Company Website: www.vexley-quill.example
Company No.: 7KQZ58
Address:
27 Bellwyn Court, Drumfiel, Kildare, Ireland, T8KN604.
Name: Colm Tierlan
Title: Chief Executive Officer
Email: ctierlan@vexley-quill.example
Phone: 00353-87-6209385

Target Market(s)

Advertisers and Marketers

Font styles to use
Serif
Script

Requirements
Must have
• Must fit dimensions given
Nice to have
• Colours that compliment our logo.

```html
<!DOCTYPE html>
<html lang="en">
<head>
<meta charset="utf-8">
<title>Vexley Quill – Business Card</title>
<link href="https://fonts.googleapis.com/css2?family=Open+Sans:wght@400;600&display=swap" rel="stylesheet">
<style>
  :root {
    --page: #e8e6e2;
    --paper: #ffffff;
    --ink: #1d1d1d;
    --card-dark: #1b1b1b;
    --pink: #e6197f;
    --orange: #e8591d;
    --green: #8cc63f;
    --muted: #3a3a3a;
  }
  * { box-sizing: border-box; margin: 0; padding: 0; }
  html, body {
    width: 1200px; height: 900px; overflow: hidden;
    background: var(--page);
    font-family: "Open Sans", sans-serif;
  }
  .sheet {
    width: 1200px; height: 900px;
    display: flex; flex-direction: column;
    align-items: center; justify-content: center; gap: 30px;
  }
  .card {
    position: relative;
    width: 620px; height: 409px;
    overflow: hidden;
  }
  .card--front { background: var(--paper); color: var(--ink); }
  .card--back { background: var(--card-dark); color: #fff; }

  .dots-area {
    position: absolute;
    border-radius: 40px;
  }
  .card--front .dots-area {
    top: 18px; right: 18px; width: 270px; height: 150px;
    background: linear-gradient(120deg, rgba(232,89,29,.55), rgba(230,25,127,.5) 50%, rgba(140,198,63,.55));
  }
  .card--back .dots-area {
    top: 0; left: 0; width: 230px; height: 230px;
    border-radius: 0 0 120px 0;
    background: linear-gradient(150deg, rgba(230,25,127,.55), rgba(232,89,29,.5) 50%, rgba(140,198,63,.5));
  }

  .wordmark {
    position: absolute;
    display: flex; align-items: center; gap: 12px;
    font-weight: 400;
    font-size: 30px;
    letter-spacing: 6px;
    text-transform: uppercase;
    white-space: nowrap;
  }
  .wordmark__dot {
    width: 26px; height: 26px; border-radius: 50%;
    background: var(--pink);
  }
  .card--front .wordmark { top: 92px; left: 46px; color: var(--ink); }
  .card--back .wordmark { bottom: 82px; right: 40px; color: #fff; }

  .person { position: absolute; left: 70px; top: 238px; }
  .person__name { font-size: 19px; font-weight: 400; color: var(--ink); }
  .person__title {
    font-size: 13px; font-weight: 400; color: var(--pink);
    text-transform: uppercase; letter-spacing: 1px; margin-top: 2px;
  }

  .details {
    position: absolute; left: 70px; top: 310px;
    display: flex; gap: 16px;
    font-size: 13px; line-height: 1.5; color: var(--muted);
  }
  .details__divider { width: 2px; background: var(--pink); }
  .details__label { color: var(--pink); margin-right: 4px; }
</style>
</head>
<body>
  <main class="sheet">
    <section class="card card--front" aria-label="Business card front">
      <div class="dots-area" role="img" aria-label="Scattered orange, pink and green dot pattern"></div>
      <div class="wordmark"><span class="wordmark__dot"></span>Vexley Quill</div>
      <div class="person">
        <p class="person__name">Colm Tierlan</p>
        <p class="person__title">Chief Executive Officer</p>
      </div>
      <div class="details">
        <address class="details__address" style="font-style:normal">
          27 Bellwyn Court<br>Drumfiel, Kildare<br>Ireland, T8KN604
        </address>
        <span class="details__divider"></span>
        <div class="details__contact">
          <span class="details__label">phone</span>00353-87-6209385<br>
          ctierlan@vexley-quill.example<br>
          www.vexley-quill.example
        </div>
      </div>
    </section>

    <section class="card card--back" aria-label="Business card back">
      <div class="dots-area" role="img" aria-label="Arc of orange, pink and green dots"></div>
      <div class="wordmark"><span class="wordmark__dot"></span>Vexley Quill</div>
    </section>
  </main>
</body>
</html>
```